Innovative Consulting Firm Needs New Business Cards and Stationary

Our Innovative Consulting Firm, Larkfield Consulting, is in need of new business cards and stationary designs. We want two-sided cards that incorporate our logo, which is attached. We are looking for something not too formal, but is professional and slick.

Card should have the following information:
Name (ex. Tom Bradley)
Title (ex. Manager)
Address (ex. 24680 Cedar Lane)
Address 2 (ex. Suite 204)
City
State
Zip Code
Mobile
Email

The card should also have our website: www.larkfieldconsulting.example

Industry/Entity Type

Management Consulting

Contact Information for Business Card

Name (ex. Tom Bradley)
Title (ex. Manager)
Address 2 (ex. Suite 204)
City
State
Zip Code
Mobile
Email

Font styles to use
Sans Serif

Requirements
Must have
• The colors on the card must match the colors in the logo. The exact color codes are attached in a pdf.
Nice to have
• The Company's Tagline is "Clarity for what comes next". This might be nice to incorporate, but not necessary.

```html
<!DOCTYPE html>
<html lang="en">
<head>
<meta charset="utf-8">
<title>Larkfield Consulting – Business Card</title>
<link rel="stylesheet" href="https://fonts.googleapis.com/css2?family=Fira+Sans+Condensed:wght@400;500&family=Courgette&display=swap">
<style>
  :root {
    --brand-blue: #0c409b;
    --brand-gold: #f0a400;
    --paper: #ffffff;
    --backdrop: #ffffff;
    --shadow: rgba(0, 0, 0, 0.35);
  }
  * { box-sizing: border-box; margin: 0; padding: 0; }
  html, body {
    width: 1200px; height: 1161px; overflow: hidden;
    background: var(--backdrop);
    font-family: "Fira Sans Condensed", "Arial Narrow", sans-serif;
  }
  .card {
    position: absolute;
    left: 161px; width: 878px; height: 528px;
    box-shadow: 6px 7px 9px var(--shadow);
  }
  .card--front {
    top: 24px;
    background: var(--paper);
    border-bottom: 3px solid var(--brand-gold);
    border-right: 2px solid var(--brand-gold);
  }
  .card--back { top: 603px; background: var(--brand-blue); }

  .holder { position: absolute; right: 84px; top: 60px; text-align: right; }
  .holder__name {
    color: var(--brand-blue); font-size: 50px; font-weight: 400; line-height: 1;
    letter-spacing: 0.5px;
  }
  .holder__title {
    margin-top: 30px; color: var(--brand-gold); font-size: 26px; font-weight: 400; line-height: 1;
  }

  .contact { position: absolute; inset: 0; }
  .contact__line {
    position: absolute; left: 146px;
    color: var(--brand-blue); font-size: 17px; letter-spacing: 0.4px; line-height: 1;
  }
  .contact__icon { position: absolute; left: 80px; fill: none; stroke: var(--brand-blue); stroke-width: 2; }

  .brand-plate {
    position: absolute; left: 242px; top: 209px; width: 394px; height: 107px;
    background: var(--paper);
    display: flex; align-items: center; justify-content: center;
  }
  .brand-plate__name {
    color: var(--brand-blue); font-size: 44px; font-weight: 500; letter-spacing: 0.5px;
  }
  .tagline {
    position: absolute; left: 0; width: 100%; top: 328px; text-align: center;
    color: var(--brand-gold);
    font-family: "Courgette", cursive; font-size: 28px; font-weight: 400; line-height: 1.2;
  }
</style>
</head>
<body>
  <section class="card card--front" aria-label="Card front">
    <div class="holder">
      <h1 class="holder__name">Tom Bradley</h1>
      <p class="holder__title">Manager</p>
    </div>

    <div class="contact">
      <svg class="contact__icon" style="top:310px" width="30" height="36" viewBox="0 0 30 36" aria-hidden="true">
        <path d="M15 34 C15 34 3 20 3 13 A12 12 0 0 1 27 13 C27 20 15 34 15 34 Z" fill="var(--brand-blue)" stroke="none"/>
        <circle cx="15" cy="13" r="4.5" fill="#fff" stroke="none"/>
      </svg>
      <span class="contact__line" style="top:301px">24680 Cedar Lane</span>
      <span class="contact__line" style="top:335px">Suite 204</span>

      <svg class="contact__icon" style="top:356px" width="30" height="30" viewBox="0 0 30 30" aria-hidden="true">
        <rect x="9" y="2" width="13" height="24" rx="2"/>
        <line x1="12" y1="22" x2="19" y2="22"/>
      </svg>
      <span class="contact__line" style="top:370px">+44 555 0192</span>

      <svg class="contact__icon" style="top:394px" width="34" height="26" viewBox="0 0 34 26" aria-hidden="true">
        <rect x="3" y="3" width="28" height="19"/>
        <polyline points="3,3 17,14 31,3"/>
      </svg>
      <span class="contact__line" style="top:404px">tombradley@larkfield.example</span>

      <svg class="contact__icon" style="top:431px" width="30" height="28" viewBox="0 0 30 28" aria-hidden="true">
        <circle cx="15" cy="14" r="11"/>
        <ellipse cx="15" cy="14" rx="5" ry="11"/>
        <line x1="4" y1="14" x2="26" y2="14"/>
        <path d="M6 8 H24 M6 20 H24"/>
      </svg>
      <span class="contact__line" style="top:438px">www.larkfieldconsulting.example</span>
    </div>
  </section>

  <section class="card card--back" aria-label="Card back">
    <div class="brand-plate">
      <span class="brand-plate__name">Larkfield Consulting</span>
    </div>
    <p class="tagline">Clarity for what comes next</p>
  </section>
</body>
</html>
```